Business Card Design Project

I help solve problems that people have with real estate, so I buy homes for cash that they no longer want, can't afford, inherited, etc. and fix and sell them or rent them or take over mortgage payments. See website: www.quickhomepurchase-example.com

Industry/Entity Type

Real Estate

Contact Information for Business Card

Not exactly sure. Looking for a design that either is similar to the website www.quickhomepurchase-example.com or that reflects what I do as described below. If it can look a little luxurious to show I can buy the houses for cash and I fix them and sell them, it's a bonus. I seem to like some of the higher end things like foil or black or something that makes it stand out.

Font styles to use
Serif

Requirements
Nice to have
• I seem to like black or clear. I like things to stand out and be different.

```html
<!DOCTYPE html>
<html lang="en">
<head>
<meta charset="utf-8">
<title>Renewed Residences – Business Card</title>
<link rel="stylesheet" href="https://fonts.googleapis.com/css2?family=Amaranth:wght@400;700&family=Roboto:wght@400;700&family=Roboto+Condensed:wght@700&display=swap">
<style>
  :root {
    --page: #ffffff;
    --card: #231f1d;
    --card-clear: #2e2a28;
    --green: #4fae2c;
    --green-light: #7cc83a;
    --green-dark: #2f7e1c;
    --silver: #d9d9d9;
    --ink-light: #f3f1e6;
    --text: #ffffff;
  }
  * { margin: 0; padding: 0; box-sizing: border-box; }
  html, body { width: 1200px; height: 657px; overflow: hidden; background: var(--page); }
  .canvas { position: relative; width: 1200px; height: 657px; }

  .card {
    position: absolute;
    width: 420px; height: 254px;
    border-radius: 16px;
    background: var(--card);
    overflow: hidden;
    font-family: "Roboto", Arial, sans-serif;
    color: var(--text);
  }
  .card--front { left: 60px; top: 64px; }
  .card--back  { left: 60px; top: 338px; }
  .card--clear { left: 650px; top: 200px; width: 430px; height: 259px; background: var(--card-clear); opacity: .96; }

  .wordmark {
    position: absolute;
    font-family: "Roboto Condensed", "Roboto", sans-serif;
    font-weight: 700;
    color: var(--green);
    line-height: .98;
    letter-spacing: 1px;
    text-transform: uppercase;
  }
  .card--front .wordmark { left: 62px; top: 78px; font-size: 44px; }
  .card--back .wordmark, .card--clear .wordmark { left: 24px; top: 92px; font-size: 36px; }

  .services {
    position: absolute; left: 0; right: 0; top: 220px;
    text-align: center; font-size: 11.5px; letter-spacing: .1px;
  }
  .services .divider { color: var(--green-light); margin: 0 5px; }

  .swoosh { position: absolute; left: 0; top: 0; width: 100%; height: 110px; }

  .person-name {
    position: absolute; right: 22px; top: 26px;
    font-family: "Amaranth", "Roboto", sans-serif;
    font-size: 19px; color: var(--ink-light);
  }

  .contact-list {
    position: absolute; left: 26px; bottom: 16px;
    list-style: none; font-size: 12px; line-height: 15px;
  }
  .contact-list li { display: flex; align-items: center; gap: 8px; }
  .contact-list svg { width: 10px; height: 10px; fill: var(--green-light); }

  .tagline {
    position: absolute; right: 22px; bottom: 16px;
    text-align: right; font-size: 12px; line-height: 15px;
  }
</style>
</head>
<body>
<main class="canvas">

  <!-- Front -->
  <section class="card card--front">
    <div class="wordmark">Renewed<br>Residences</div>
    <p class="services">BUY A HOME<span class="divider">|</span>FACING FORECLOSURE<span class="divider">|</span>SELL A HOME</p>
  </section>

  <!-- Back -->
  <section class="card card--back">
    <svg class="swoosh" viewBox="0 0 420 110" preserveAspectRatio="none" aria-hidden="true">
      <defs>
        <linearGradient id="greenBand" x1="0" y1="0" x2="0" y2="1">
          <stop offset="0" stop-color="var(--green-light)"/>
          <stop offset="1" stop-color="var(--green-dark)"/>
        </linearGradient>
      </defs>
      <path d="M0,0 H420 V96 C330,112 270,92 200,56 C140,26 60,26 0,52 Z" fill="var(--silver)"/>
      <path d="M0,0 H420 V92 C330,104 270,84 200,48 C140,20 60,22 0,46 Z" fill="#141110"/>
      <path d="M0,0 H420 V86 C330,96 270,76 205,40 C150,12 60,14 0,38 Z" fill="url(#greenBand)"/>
      <path d="M30,40 C90,18 150,24 205,52 C150,30 90,26 30,40 Z" fill="var(--silver)"/>
    </svg>
    <h2 class="person-name">Dana L. Morrow</h2>
    <div class="wordmark">Renewed<br>Residences</div>
    <ul class="contact-list">
      <li><svg viewBox="0 0 10 10"><path d="M1 3 Q5 0 9 3 V4.5 H7 V3.5 H3 V4.5 H1 Z M2 5 H8 L9 9 H1 Z"/></svg>555-014-SOLD</li>
      <li><svg viewBox="0 0 10 10"><path d="M0 2 H10 V8 H0 Z M0.8 2.6 L5 5.6 L9.2 2.6" stroke="var(--card)" stroke-width=".8"/></svg>Dana@quickhomepurchase-example.com</li>
      <li><svg viewBox="0 0 10 10"><circle cx="5" cy="5" r="4.5"/><path d="M0.5 5 H9.5 M5 0.5 V9.5 M5 0.5 Q2 5 5 9.5 Q8 5 5 0.5" stroke="var(--card)" stroke-width=".6" fill="none"/></svg>www.quickhomepurchase-example.com</li>
    </ul>
    <p class="tagline">Buying and Selling<br>Homes in Your Area</p>
  </section>

  <!-- Clear stock variant -->
  <section class="card card--clear">
    <svg class="swoosh" viewBox="0 0 420 110" preserveAspectRatio="none" aria-hidden="true">
      <defs>
        <linearGradient id="greenBandClear" x1="0" y1="0" x2="0" y2="1">
          <stop offset="0" stop-color="var(--green-light)"/>
          <stop offset="1" stop-color="var(--green-dark)"/>
        </linearGradient>
      </defs>
      <path d="M0,0 H420 V96 C330,112 270,92 200,56 C140,26 60,26 0,52 Z" fill="var(--silver)"/>
      <path d="M0,0 H420 V92 C330,104 270,84 200,48 C140,20 60,22 0,46 Z" fill="#141110"/>
      <path d="M0,0 H420 V86 C330,96 270,76 205,40 C150,12 60,14 0,38 Z" fill="url(#greenBandClear)"/>
      <path d="M30,40 C90,18 150,24 205,52 C150,30 90,26 30,40 Z" fill="var(--silver)"/>
    </svg>
    <h2 class="person-name">Dana L. Morrow</h2>
    <div class="wordmark">Renewed<br>Residences</div>
    <ul class="contact-list">
      <li><svg viewBox="0 0 10 10"><path d="M1 3 Q5 0 9 3 V4.5 H7 V3.5 H3 V4.5 H1 Z M2 5 H8 L9 9 H1 Z"/></svg>555-014-SOLD</li>
      <li><svg viewBox="0 0 10 10"><path d="M0 2 H10 V8 H0 Z M0.8 2.6 L5 5.6 L9.2 2.6" stroke="var(--card-clear)" stroke-width=".8"/></svg>Dana@quickhomepurchase-example.com</li>
      <li><svg viewBox="0 0 10 10"><circle cx="5" cy="5" r="4.5"/><path d="M0.5 5 H9.5 M5 0.5 V9.5 M5 0.5 Q2 5 5 9.5 Q8 5 5 0.5" stroke="var(--card-clear)" stroke-width=".6" fill="none"/></svg>www.quickhomepurchase-example.com</li>
    </ul>
    <p class="tagline">Buying and Selling<br>Homes in Your Area</p>
  </section>

</main>
</body>
</html>
```